V9 Web Design Project

New company website for Intel cyber security company.

Style should be cool, but remain appropriate for very serious subject matter and audience.

Target Market(s)

Target audience is government and the military

Navigation needs to include:
- About Us
- Services
- Careers
- Contact Us
- Contracts

As well as 2 feature areas - use "Technology Integration" and "Case Study" as the supporting headlines.

Industry/Entity Type

Security

Font styles to use
Sans Serif

Colors

Designer to choose colors to be used in the design.

Requirements
Must have
• Mountain imagery and theme.

Use logo attached.

New Tagline - "Securing the Continuum"
Nice to have
• Supporting imagery could include photos representative of security - avoid cliches.
Should not have
• Needs to be serious not frivolous

```html
<!DOCTYPE html>
<html lang="en">
<head>
<meta charset="utf-8">
<title>V9 Group — Securing the Continuum</title>
<link href="https://fonts.googleapis.com/css2?family=Questrial&family=Lato:ital,wght@0,400;0,700;1,400&display=swap" rel="stylesheet">
<style>
  :root {
    --navy: #1e2b5a;
    --ink: #333a45;
    --muted: #7d8794;
    --heading: #8fa4b6;
    --accent: #1f8ad0;
    --rule: #d9dee3;
    --panel: #f1f3f5;
    --footer: #2e2f31;
    --white: #ffffff;
  }
  * { box-sizing: border-box; margin: 0; padding: 0; }
  html, body { width: 744px; height: 1200px; overflow: hidden; background: var(--white); }
  body { position: relative; font-family: "Questrial", sans-serif; color: var(--ink); }
  h1, h2, h3 { font-weight: normal; }

  .site-header { position: absolute; top: 0; left: 0; width: 744px; height: 42px; background: var(--white); border-bottom: 1px solid #c9ced4; }
  .brand { position: absolute; left: 82px; top: 5px; display: flex; align-items: center; gap: 8px; }
  .brand-mark { width: 32px; height: 32px; background: linear-gradient(160deg, #cfd6de, #55606e 60%, #2c3440); }
  .brand-name { font-size: 18px; color: var(--navy); letter-spacing: 0.3px; }
  .main-nav { position: absolute; right: 80px; top: 0; height: 42px; display: flex; align-items: center; }
  .main-nav a { font-size: 9px; color: var(--ink); text-decoration: none; padding: 0 11px; border-left: 1px solid #e4e7ea; line-height: 16px; }
  .main-nav a:first-child { border-left: none; }

  .hero { position: absolute; top: 42px; left: 0; width: 744px; height: 295px;
    background: linear-gradient(180deg, #3f6277 0%, #8ea8b3 35%, #c9cfcd 55%, #b89a72 72%, #3a4a73 88%, #27305a 100%); }
  .hero-title { position: absolute; top: 60px; width: 100%; text-align: center; font-size: 28px; color: var(--white); letter-spacing: 0.5px; }
  .hero-sub { position: absolute; top: 101px; left: 214px; width: 316px; text-align: center; font-family: "Lato", sans-serif; font-size: 13px; line-height: 18px; color: var(--white); }

  .clients { position: absolute; top: 337px; left: 0; width: 744px; height: 68px; border-bottom: 1px solid #e6e9ec; }
  .merchants { position: absolute; left: 110px; top: 20px; text-align: center; }
  .merchants-count { font-size: 14px; color: var(--ink); line-height: 16px; }
  .merchants-count b { font-weight: normal; color: var(--accent); font-size: 16px; }
  .merchants-note { font-size: 8.5px; color: var(--ink); }
  .partner { position: absolute; top: 25px; font-size: 15px; color: #8a8f96; font-weight: bold; font-family: "Lato", sans-serif; }

  .section-heading { text-align: center; font-size: 14px; letter-spacing: 1.2px; color: var(--heading); }
  .section-heading .slash { color: var(--navy); margin-right: 3px; }
  .section-text { width: 500px; margin: 0 auto; text-align: center; font-size: 9.5px; line-height: 19px; color: var(--muted); }

  .tech { position: absolute; top: 405px; left: 0; width: 744px; height: 216px; }
  .tech .section-heading { margin-top: 31px; }
  .tech .section-text { margin-top: 17px; }
  .btn-outline { position: absolute; left: 302px; top: 152px; width: 140px; height: 27px; border: 1px solid #cdd3d9; border-radius: 2px; font-size: 9.5px; color: var(--muted); display: flex; align-items: center; justify-content: center; letter-spacing: 0.3px; }

  .case { position: absolute; top: 621px; left: 0; width: 744px; height: 315px; background: var(--panel); border-top: 1px solid #dde1e5; border-bottom: 1px solid #dde1e5; }
  .case-emblem { position: absolute; left: 309px; top: 40px; width: 122px; height: 122px; border-radius: 50%;
    background: radial-gradient(circle at 50% 95%, #c9a05c 0%, #2f6f80 45%, #1c4c6e 75%); }
  .case .section-heading { position: absolute; top: 197px; width: 100%; }
  .case .section-text { position: absolute; top: 227px; left: 122px; }

  .widgets { position: absolute; top: 936px; left: 0; width: 744px; height: 221px; }
  .widget { position: absolute; top: 32px; height: 170px; }
  .widget-title { font-size: 13px; color: var(--heading); letter-spacing: 0.8px; height: 21px; border-bottom: 1px solid var(--rule); position: relative; }
  .widget-title::after { content: ""; position: absolute; left: 0; bottom: -1px; width: 31px; height: 2px; background: var(--accent); }
  .widget-link { position: absolute; right: 8px; top: 4px; font-size: 8px; color: var(--accent); letter-spacing: 0; }
  .col-divider { position: absolute; top: 12px; width: 1px; height: 170px; background: var(--rule); }

  .quote { position: absolute; top: 44px; left: 0; width: 168px; height: 74px; border: 1px solid #d6dbe0; padding: 8px 6px; font-family: "Lato", sans-serif; font-style: italic; font-size: 7.5px; line-height: 12px; color: var(--ink); }
  .quote-mark { color: #c4cad0; font-size: 11px; line-height: 0; }
  .quote-author { position: absolute; left: 90px; top: 126px; font-family: "Lato", sans-serif; font-style: italic; font-size: 7.5px; color: var(--navy); }
  .dots { position: absolute; top: 158px; left: 2px; display: flex; gap: 4px; }
  .dots span { width: 4px; height: 4px; border-radius: 50%; background: #c8cdd2; }
  .dots span:first-child { background: var(--accent); }

  .news-item { display: flex; gap: 7px; padding: 10px 0 6px; border-bottom: 1px dotted #c9ced3; width: 178px; font-family: "Lato", sans-serif; font-size: 7.5px; line-height: 10.3px; color: var(--ink); }
  .news-item strong { font-weight: normal; color: var(--accent); display: block; }

  .tweet { display: flex; gap: 8px; margin-top: 12px; }
  .tweet-dot { width: 12px; height: 12px; border-radius: 50%; background: #4fa4de; margin-top: 6px; flex: none; }
  .tweet-body { width: 145px; }
  .tweet-bubble { border: 1px solid #d6dbe0; border-radius: 2px; padding: 6px 6px; font-family: "Lato", sans-serif; font-size: 7.3px; line-height: 10.3px; color: var(--ink); }
  .tweet-meta { display: flex; justify-content: space-between; font-family: "Lato", sans-serif; font-size: 6.5px; color: var(--muted); padding: 3px 0 0 4px; }
  .tweet-meta span:last-child { color: var(--accent); }

  .site-footer { position: absolute; top: 1157px; left: 0; width: 744px; height: 43px; background: var(--footer); }
  .footer-links { position: absolute; left: 82px; top: 15px; font-size: 9px; color: #9a9da2; }
  .footer-links .sep { margin: 0 5px; }
  .footer-brand { position: absolute; right: 80px; top: 9px; display: flex; align-items: center; gap: 7px; }
  .footer-brand .brand-mark { width: 24px; height: 24px; opacity: 0.7; }
  .footer-brand .brand-name { font-size: 14px; color: #a2a6ab; }
</style>
</head>
<body>
  <header class="site-header">
    <div class="brand">
      <div class="brand-mark" role="img" aria-label="Snowy mountain peak photo"></div>
      <span class="brand-name">V9 GROUP</span>
    </div>
    <nav class="main-nav">
      <a href="#">About Us</a><a href="#">Services</a><a href="#">Careers</a><a href="#">Contact Us</a><a href="#">Contracts</a>
    </nav>
  </header>

  <section class="hero" role="img" aria-label="Snow-capped mountain range above a sea of clouds at dusk">
    <h1 class="hero-title">Securing the Continuum</h1>
    <p class="hero-sub">Lorem Ipsum is simply dummy text of the printing<br>and typesetting industry.</p>
  </section>

  <section class="clients">
    <div class="merchants">
      <div class="merchants-count"><b>174</b> merchants</div>
      <div class="merchants-note">already using Brevlo – join them</div>
    </div>
    <span class="partner" style="left:305px">Framehall</span>
    <span class="partner" style="left:421px">Slatework</span>
    <span class="partner" style="left:524px">Tonecraft</span>
  </section>

  <section class="tech">
    <h2 class="section-heading"><span class="slash">/</span>TECHNOLOGY INTEGRATION</h2>
    <p class="section-text">Lorem Ipsum is simply dummy text of the printing and typesetting industry. Lorem Ipsum has been the industry's standard dummy text ever since the 1500s, when an unknown printer took a galley of type and scrambled it to make a type specimen book. It has survived not only five centuries.</p>
    <a class="btn-outline">READ MORE</a>
  </section>

  <section class="case" role="img" aria-label="Faded photo of an open book under a magnifying glass">
    <div class="case-emblem" role="img" aria-label="Illustration of a head in profile with a lightbulb idea"></div>
    <h2 class="section-heading"><span class="slash">/</span>CASE STUDY</h2>
    <p class="section-text">Lorem Ipsum is simply dummy text of the printing and typesetting industry. Lorem Ipsum has been the industry's standard dummy text ever since the 1500s, when an unknown printer took a galley of type and scrambled it to make a type specimen book. It has survived not only five centuries.</p>
  </section>

  <section class="widgets">
    <div class="widget" style="left:86px;width:169px">
      <h3 class="widget-title">CLIENT&nbsp; SPEAK</h3>
      <blockquote class="quote"><span class="quote-mark">“</span> Lorem Ipsum is simply dummy text of the printing and typesetting industry. Lorem Ipsum has been the industry's standard dummy text ever since the 1500s <span class="quote-mark">”</span></blockquote>
      <div class="quote-author">John Doe</div>
      <div class="dots"><span></span><span></span><span></span><span></span></div>
    </div>
    <div class="col-divider" style="left:272px"></div>
    <div class="widget" style="left:287px;width:180px">
      <h3 class="widget-title">LATEST NEWS<span class="widget-link">View more &gt;</span></h3>
      <div class="news-item">
        <svg width="18" height="18" viewBox="0 0 18 18" fill="none" stroke="#9aa5b0" stroke-width="1"><rect x="1.5" y="3" width="15" height="13.5" rx="1"/><line x1="5" y1="1" x2="5" y2="5"/><line x1="13" y1="1" x2="13" y2="5"/><path d="M5 8h1M8.5 8h1M12 8h1M5 11h1M8.5 11h1M12 11h1M5 14h1M8.5 14h1"/></svg>
        <div><strong>Lorem Ipsum is simply dummy text of the printing and typesetting industry.</strong>Lorem Ipsum has been the industry's standard dummy text ever since the</div>
      </div>
      <div class="news-item">
        <svg width="18" height="18" viewBox="0 0 18 18" fill="none" stroke="#9aa5b0" stroke-width="1"><rect x="1.5" y="3" width="15" height="13.5" rx="1"/><line x1="5" y1="1" x2="5" y2="5"/><line x1="13" y1="1" x2="13" y2="5"/><path d="M5 8h1M8.5 8h1M12 8h1M5 11h1M8.5 11h1M12 11h1M5 14h1M8.5 14h1"/></svg>
        <div><strong>Lorem Ipsum is simply dummy text of the printing and typesetting industry.</strong>Lorem Ipsum has been the industry's standard dummy text ever since the</div>
      </div>
    </div>
    <div class="col-divider" style="left:474px"></div>
    <div class="widget" style="left:489px;width:170px">
      <h3 class="widget-title">CHIRPLINE FEED</h3>
      <div class="tweet">
        <span class="tweet-dot"></span>
        <div class="tweet-body">
          <div class="tweet-bubble">Lorem Ipsum is simply dummy text of the printing and typesetting industry. Lorem Ipsum has been the industry's</div>
          <div class="tweet-meta"><span>20 minutes ago</span><span>@V9 Group</span></div>
        </div>
      </div>
      <div class="tweet">
        <span class="tweet-dot"></span>
        <div class="tweet-body">
          <div class="tweet-bubble">Lorem Ipsum is simply dummy text of the printing and typesetting industry. Lorem Ipsum has been the industry's</div>
          <div class="tweet-meta"><span>3 hours ago</span><span>@V9 Group</span></div>
        </div>
      </div>
    </div>
  </section>

  <footer class="site-footer">
    <div class="footer-links">© V9 Group<span class="sep">/</span>Terms<span class="sep">/</span>Privacy</div>
    <div class="footer-brand">
      <div class="brand-mark" role="img" aria-label="Snowy mountain peak photo"></div>
      <span class="brand-name">V9 GROUP</span>
    </div>
  </footer>
</body>
</html>
```